Website Design mainly for sliders and icons

Two pages need to be designe, I've finished the templates, all detail requirement please check inattachment:

Mainly design: some pictures/icons and frames

```html
<!DOCTYPE html>
<html lang="en">
<head>
<meta charset="utf-8">
<title>Tidecloud</title>
<link rel="stylesheet" href="https://fonts.googleapis.com/css2?family=Didact+Gothic&family=Open+Sans:wght@400;600;700&display=swap">
<style>
:root{
  --blue:#0aa6e6;
  --blue-dark:#0891cc;
  --ink:#222;
  --muted:#555;
  --cream:#efece0;
  --band:#e9e9e9;
  --dots:#9b978b;
  --white:#fff;
}
*{box-sizing:border-box;margin:0;padding:0}
html,body{width:768px;height:1200px;overflow:hidden;background:var(--white)}
body{position:relative;font-family:"Didact Gothic",sans-serif;color:var(--ink)}
.abs{position:absolute}

/* top bar */
.topbar{left:0;top:0;width:768px;height:27px;background:var(--blue)}
.social{left:110px;top:8px;display:flex;gap:5px}
.social span{width:11px;height:11px;border-radius:50%;background:var(--white);display:block}
.nav{right:78px;top:0;height:27px;display:flex;align-items:center;gap:14px;color:var(--white);font-family:"Open Sans",sans-serif;font-size:10.5px}
.nav .sep{opacity:.9}

/* header */
.brand{left:101px;top:40px;font-size:24px;color:var(--ink);letter-spacing:.5px}
.contact{top:44px;display:flex;align-items:center;gap:6px;color:var(--blue);font-size:13px;letter-spacing:.5px}
.contact .ico{width:20px;height:20px;border-radius:3px;background:var(--blue);display:flex;align-items:center;justify-content:center}
.phone{left:372px}
.mail{left:520px}

/* slider */
.slider{left:101px;top:81px;width:563px;height:89px;border:2px solid var(--blue);background:var(--band)}
.slide{top:7px;width:145px;height:71px;border:2px solid var(--blue);background:var(--white);padding:4px}
.slide .art{width:100%;height:100%}
.arrow{top:32px}

/* hero band */
.hero{left:0;top:178px;width:768px;height:281px;background:var(--band);border-bottom:3px solid var(--blue)}
.note{width:170px;padding:4px 4px;background:var(--cream);border-top:3px solid var(--blue);font-size:8.2px;line-height:9.4px;text-align:center;color:var(--ink)}
.hero-figure{left:300px;top:197px;width:167px;height:259px;background:linear-gradient(180deg,#e9e9e9 0%,#f3d55a 14%,#f4f4f4 32%,#e6e6e6 70%,#222 100%);border-radius:40px 40px 0 0}
.hero-q{left:428px;top:188px;font-size:40px;color:var(--blue);font-family:"Open Sans",sans-serif}

/* choose */
.choose-title{left:269px;top:472px;width:230px;height:28px;background:var(--blue);color:var(--white);font-family:"Open Sans",sans-serif;font-weight:700;font-size:14px;display:flex;align-items:center;justify-content:center}
.choose-intro{left:100px;top:513px;width:568px;font-size:7.6px;line-height:11.5px;text-align:center;font-family:"Open Sans",sans-serif}
.steps{left:0;top:550px;width:768px;height:145px}
.step-card{top:692px;height:105px;background:var(--cream);border-top:3px solid var(--blue);border-bottom:3px solid var(--blue);padding:3px 4px;font-size:8.2px;line-height:9.4px;text-align:center}

/* customers & partners */
.section-title{top:834px;font-family:"Open Sans",sans-serif;font-weight:600;font-size:19px;color:var(--blue)}
.org-name{font-size:13px;color:var(--blue);display:flex;align-items:center;gap:4px;width:80px}
.org-name i{width:8px;height:8px;background:var(--blue);display:block;flex:none}
.org-text{width:135px;font-family:"Open Sans",sans-serif;font-size:7.2px;line-height:10.5px;color:var(--blue)}
.org-text b{font-weight:700}
.badge{border-radius:3px}

/* footer */
.footer{left:0;top:1170px;width:768px;height:30px;background:var(--blue);color:var(--white);font-family:"Open Sans",sans-serif;font-size:10px;display:flex;align-items:center;justify-content:center;gap:8px}
</style>
</head>
<body>

<header>
  <div class="abs topbar"></div>
  <div class="abs social"><span></span><span></span><span></span><span></span></div>
  <nav class="abs nav">
    <svg width="10" height="9" viewBox="0 0 10 9"><path d="M5 0 10 4.5H8.5V9H6V6H4V9H1.5V4.5H0Z" fill="#fff"/></svg>
    <span class="sep">|</span><span>Solution</span><span class="sep">|</span><span>About Us</span><span class="sep">|</span><span>Contact Us</span><span class="sep">|</span><span>News</span>
  </nav>
  <div class="abs brand">Tidecloud</div>
  <div class="abs contact phone">
    <span class="ico"><svg width="12" height="12" viewBox="0 0 12 12"><path d="M3 1 5 3.5 4 5c.8 1.5 1.7 2.4 3 3l1.5-1L11 9l-1 2C6 11 1 6 1 2Z" fill="#fff"/></svg></span>
    <span>xxxxx - xxxxxxxx</span>
  </div>
  <div class="abs contact mail">
    <span class="ico"><svg width="12" height="10" viewBox="0 0 12 10"><rect x="1" y="1" width="10" height="8" fill="none" stroke="#fff" stroke-width="1.2"/><path d="M1 1 6 5.5 11 1" fill="none" stroke="#fff" stroke-width="1.2"/></svg></span>
    <span>xxxxx@xxxx.com</span>
  </div>
</header>

<section class="abs slider">
  <svg class="abs arrow" style="left:11px" width="17" height="20" viewBox="0 0 17 20"><path d="M17 0V20L0 10Z" fill="var(--blue)"/></svg>
  <div class="abs slide" style="left:42px"><div class="art" role="img" aria-label="Server tower with stacked storage drums" style="background:linear-gradient(90deg,#fff 25%,#2a2f38 40%,#3fa9e0 60%,#fff 80%)"></div></div>
  <div class="abs slide" style="left:205px"><div class="art" role="img" aria-label="Two hands in a handshake" style="background:linear-gradient(90deg,#fff 20%,#3b5f9a 35%,#f2a25a 50%,#3b5f9a 65%,#fff 80%)"></div></div>
  <div class="abs slide" style="left:368px"><div class="art" role="img" aria-label="Server rack resting on clouds" style="background:linear-gradient(180deg,#fff 5%,#3a3d44 30%,#6c7079 60%,#d6e8f4 85%)"></div></div>
  <svg class="abs arrow" style="left:530px" width="17" height="20" viewBox="0 0 17 20"><path d="M0 0V20L17 10Z" fill="var(--blue)"/></svg>
</section>

<section class="abs hero">
  <p class="abs note" style="left:101px;top:29px">Lorem Ipsum is simply dummy text of the printing and typesetting industry. Lorem Ipsum has been the industry's standard dummy text ever since the 1500s, when an unknown printer took a galley of type and scrambled it to make a type specimen book. It has survived not only five centuries, but also the leap into electronic typesetting, remaining essentially unchanged.</p>
  <p class="abs note" style="left:101px;top:152px">Lorem Ipsum is simply dummy text of the printing and typesetting industry. Lorem Ipsum has been the industry's standard dummy text ever since the 1500s, when an unknown printer took a galley of type and scrambled it to make a type specimen book. It has survived not only five centuries, but also the leap into electronic typesetting, remaining essentially unchanged.</p>
  <p class="abs note" style="left:495px;top:29px">Lorem Ipsum is simply dummy text of the printing and typesetting industry. Lorem Ipsum has been the industry's standard dummy text ever since the 1500s, when an unknown printer took a galley of type and scrambled it to make a type specimen book. It has survived not only five centuries, but also the leap into electronic typesetting, remaining essentially unchanged.</p>
  <p class="abs note" style="left:495px;top:152px">Lorem Ipsum is simply dummy text of the printing and typesetting industry. Lorem Ipsum has been the industry's standard dummy text ever since the 1500s, when an unknown printer took a galley of type and scrambled it to make a type specimen book. It has survived not only five centuries, but also the leap into electronic typesetting, remaining essentially unchanged.</p>
</section>
<div class="abs hero-figure" role="img" aria-label="Engineer in a yellow hard hat holding rolled plans, arms crossed"></div>
<div class="abs hero-q">?</div>

<h2 class="abs choose-title">Please Choose Tidecloud !</h2>
<p class="abs choose-intro">Lorem Ipsum is simply dummy text of the printing and typesetting industry. Lorem Ipsum has been the industry's standard dummy text ever since the 1500s,<br>when an unknown as printer took a galley of type and scrambled it to make a type specimen book. It has survived not only five centuries,<br>but also the leap into electronic typesetting, remaining essentially unchanged. It was popularised in the 1960s with the release</p>

<svg class="abs steps" viewBox="0 550 768 145" width="768" height="145">
  <g stroke="var(--dots)" stroke-width="4" stroke-dasharray="4 3">
    <line x1="240" y1="602" x2="339" y2="602"/>
    <line x1="439" y1="602" x2="524" y2="602"/>
    <line x1="190" y1="660" x2="190" y2="690"/>
    <line x1="389" y1="660" x2="389" y2="690"/>
    <line x1="574" y1="660" x2="574" y2="690"/>
  </g>
  <g fill="var(--cream)" stroke="#d8d3bf" stroke-width="2">
    <circle cx="190" cy="602" r="47"/>
    <circle cx="389" cy="602" r="47"/>
    <circle cx="574" cy="602" r="47"/>
  </g>
  <!-- consulting: people -->
  <g fill="var(--blue)">
    <circle cx="178" cy="574" r="5"/><circle cx="192" cy="571" r="6"/><circle cx="207" cy="574" r="5"/>
    <rect x="170" y="581" width="14" height="26" rx="3"/><rect x="185" y="579" width="15" height="34" rx="3"/><rect x="201" y="581" width="14" height="26" rx="3"/>
  </g>
  <!-- deploying: crossing arrows -->
  <g fill="none" stroke="var(--blue)" stroke-width="6">
    <path d="M360 581h10l24 34h12"/><path d="M360 615h10l24-34h12"/>
  </g>
  <g fill="var(--blue)"><path d="M404 572l14 9-14 9Z"/><path d="M404 606l14 9-14 9Z"/></g>
  <!-- integration: puzzle pieces -->
  <g fill="var(--blue)">
    <path d="M540 584h12a5 5 0 1 1 8 0h10v12a5 5 0 1 0 0 8v12h-30Z"/>
    <path d="M576 580h26v12a5 5 0 1 0 0 8v10h-12a5 5 0 1 1-8 0h-6Z" transform="rotate(10 590 595)"/>
  </g>
  <!-- ribbons -->
  <g fill="var(--blue)">
    <path d="M141 628h101l-7 8 7 8H141l7-8Z"/>
    <path d="M339 628h100l-7 8 7 8H339l7-8Z"/>
    <path d="M524 628h101l-7 8 7 8H524l7-8Z"/>
  </g>
  <g fill="#fff" font-family="Open Sans, sans-serif" font-weight="700" font-size="9.5" text-anchor="middle" letter-spacing=".6">
    <text x="191" y="639.5">CONSULTING</text>
    <text x="389" y="639.5">DEPLOYING</text>
    <text x="575" y="639.5">INTEGRATION</text>
  </g>
</svg>

<p class="abs step-card" style="left:101px;width:177px">Lorem Ipsum is simply dummy text of the printing and typesetting industry. Lorem Ipsum has been the industry's standard dummy text ever since the 1500s, when an unknown printer took a galley of type and scrambled it to make a type specimen book. It has survived not only five centuries, but also the leap into electronic typesetting, remaining essentially unchanged.</p>
<p class="abs step-card" style="left:296px;width:176px">Lorem Ipsum is simply dummy text of the printing and typesetting industry. Lorem Ipsum has been the industry's standard dummy text ever since the 1500s, when an unknown printer took a galley of type and scrambled it to make a type specimen book. It has survived not only five centuries, but also the leap into electronic typesetting, remaining essentially unchanged.</p>
<p class="abs step-card" style="left:487px;width:177px">Lorem Ipsum is simply dummy text of the printing and typesetting industry. Lorem Ipsum has been the industry's standard dummy text ever since the 1500s, when an unknown printer took a galley of type and scrambled it to make a type specimen book. It has survived not only five centuries, but also the leap into electronic typesetting, remaining essentially unchanged.</p>

<section class="customers">
  <h3 class="abs section-title" style="left:107px">Our Customers</h3>
  <div class="abs org-name" style="left:110px;top:910px"><i></i>Nimbus Nine</div>
  <p class="abs org-text" style="left:198px;top:902px"><b>Nimbus Nine</b> is a China-based one-stop cloud solution provider, with more than 10 years' experience of cloud deployment, management and operation.</p>
  <div class="abs org-name" style="left:110px;top:976px"><i></i>Stackwell</div>
  <p class="abs org-text" style="left:198px;top:972px"><b>Stackwell</b> is a China-based one-stop cloud solution provider, with more than 10 years' experience of cloud deployment, management and operation.</p>
  <div class="abs badge" style="left:119px;top:1028px;width:40px;height:40px;background:#e9eef2"></div>
  <p class="abs org-text" style="left:198px;top:1034px"><b>Orbit Network</b> is a China-based one-stop cloud solution provider, with more than 10 years' experience of cloud deployment, management and operation.</p>
</section>

<section class="partners">
  <h3 class="abs section-title" style="left:402px">Our Partners</h3>
  <div class="abs org-name" style="left:402px;top:907px;width:80px;height:30px;background:var(--blue);color:#fff;justify-content:center;border-radius:2px">Verapath</div>
  <p class="abs org-text" style="left:503px;top:902px"><b>Verapath</b> is a China-based one-stop cloud solution provider, with more than 10 years' experience of cloud deployment, management and operation.</p>
  <div class="abs org-name" style="left:420px;top:972px;gap:5px"><i style="border-radius:50%;width:10px;height:10px"></i>Halvern</div>
  <p class="abs org-text" style="left:503px;top:968px"><b>Halvern</b> is a China-based one-stop cloud solution provider, with more than 10 years' experience of cloud deployment, management and operation.</p>
</section>

<footer class="abs footer">
  <span>2014 Tidecloud Limited</span><span>|</span><span>Tel : XXXXXXXXXXX</span><span>|</span><span>support@tidecloud.example</span>
</footer>

</body>
</html>
```